Harlow Pennick Group Business Cards

We have a new logo, and want to design new business cards with it. We are 21 years in business, and want a fresh but professional look, so not a lot of extra stuff on the card. We are a recruiting and staffing firm focused on placing accounting and finance professionals in the Dallas TX area. I've attached our new logo that should be displayed on the cards. Here is what I think we want on the cards:
Ned Varcombe, CPA
Partner and Managing Director
8262 Quarry Mill Rd.
Suite 610
Dallas, TX 75391
O 214-583-9071
M 214-690-1482
ned@harlowpennick-example.com
www.harlowpennick-example.com

```html
<!DOCTYPE html>
<html lang="en">
<head>
<meta charset="utf-8">
<title>Harlow Pennick Group Business Cards</title>
<link rel="stylesheet" href="https://fonts.googleapis.com/css2?family=Montserrat:wght@700&family=Open+Sans:wght@400;600;700&display=swap">
<style>
  :root {
    --brand-blue: #0d3fb3;
    --brand-blue-deep: #0a3499;
    --accent-blue: #4a74d8;
    --ink-grey: #4a4a4a;
    --card-white: #ffffff;
    --backdrop: #e4e5e8;
  }
  * { box-sizing: border-box; margin: 0; padding: 0; }
  html, body {
    width: 1200px;
    height: 959px;
    overflow: hidden;
    background: var(--backdrop);
    font-family: "Open Sans", Arial, sans-serif;
  }
  .canvas {
    position: relative;
    width: 1200px;
    height: 959px;
  }
  .card {
    position: absolute;
    left: 250px;
    width: 700px;
    height: 400px;
    box-shadow: 0 6px 18px rgba(0,0,0,0.18);
    overflow: hidden;
  }
  /* Front card */
  .card-front {
    top: 60px;
    background: linear-gradient(135deg, #1050c4 0%, var(--brand-blue) 55%, var(--brand-blue-deep) 100%);
  }
  .front-wordmark {
    position: absolute;
    top: 150px;
    left: 0;
    width: 100%;
    text-align: center;
    color: var(--card-white);
    font-family: "Montserrat", Arial, sans-serif;
    font-weight: 700;
    font-size: 46px;
    letter-spacing: 1px;
  }
  .front-website {
    position: absolute;
    left: 60px;
    bottom: 70px;
    color: var(--card-white);
    font-size: 15px;
    letter-spacing: 6px;
  }
  /* Back card */
  .card-back {
    top: 500px;
    background: var(--card-white);
  }
  .card-back svg.rules {
    position: absolute;
    inset: 0;
  }
  .name-block {
    position: absolute;
    top: 36px;
    left: 38px;
    color: var(--card-white);
  }
  .person-name {
    font-size: 22px;
    font-weight: 700;
    line-height: 1.15;
  }
  .person-title {
    font-size: 14px;
    font-weight: 400;
  }
  .back-wordmark {
    position: absolute;
    right: 40px;
    top: 136px;
    color: var(--brand-blue);
    font-family: "Montserrat", Arial, sans-serif;
    font-weight: 700;
    font-size: 26px;
    line-height: 1.1;
    text-align: right;
  }
  .contact-list {
    position: absolute;
    left: 34px;
    top: 166px;
    list-style: none;
    color: var(--ink-grey);
    font-size: 16px;
    line-height: 1.55;
  }
  .contact-list li {
    display: flex;
    align-items: center;
    gap: 8px;
  }
  .contact-list svg { flex: none; }
  .address {
    position: absolute;
    right: 40px;
    bottom: 48px;
    text-align: right;
    color: var(--ink-grey);
    font-size: 18px;
    font-style: normal;
    line-height: 1.35;
  }
</style>
</head>
<body>
<main class="canvas">
  <section class="card card-front" aria-label="Business card front">
    <div class="front-wordmark">Harlow Pennick Group</div>
    <div class="front-website">www.harlowpennick-example.com</div>
  </section>

  <section class="card card-back" aria-label="Business card back">
    <svg class="rules" width="700" height="400" viewBox="0 0 700 400" aria-hidden="true">
      <polygon points="0,26 20,26 20,108 0,108" fill="var(--accent-blue)"/>
      <polygon points="20,26 330,26 368,108 20,108" fill="var(--brand-blue)"/>
      <polyline points="368,108 418,210 660,210" fill="none" stroke="var(--brand-blue)" stroke-width="1.5"/>
    </svg>

    <div class="name-block">
      <div class="person-name">Ned Varcombe, CPA</div>
      <div class="person-title">Partner &amp; Managing Director</div>
    </div>

    <div class="back-wordmark">Harlow Pennick<br>Group</div>

    <ul class="contact-list">
      <li>
        <svg width="14" height="14" viewBox="0 0 24 24" aria-hidden="true"><path fill="var(--brand-blue)" d="M6.6 10.8a15.1 15.1 0 0 0 6.6 6.6l2.2-2.2c.3-.3.7-.4 1-.2 1.1.4 2.3.6 3.6.6.6 0 1 .4 1 1V20c0 .6-.4 1-1 1A17 17 0 0 1 3 4c0-.6.4-1 1-1h3.5c.6 0 1 .4 1 1 0 1.3.2 2.5.6 3.6.1.3 0 .7-.2 1z"/></svg>
        O 214-583-9071
      </li>
      <li>
        <svg width="14" height="14" viewBox="0 0 24 24" aria-hidden="true"><path fill="var(--brand-blue)" d="M7 1h10c1.1 0 2 .9 2 2v18c0 1.1-.9 2-2 2H7c-1.1 0-2-.9-2-2V3c0-1.1.9-2 2-2zm0 3v14h10V4z"/></svg>
        M 214-690-1482
      </li>
      <li>
        <svg width="14" height="14" viewBox="0 0 24 24" aria-hidden="true"><path fill="var(--brand-blue)" d="M2 5h20v14H2z M2 5l10 8 10-8" stroke="#fff" stroke-width="1.5"/></svg>
        ned@harlowpennick-example.com
      </li>
    </ul>

    <address class="address">
      8262 Quarry Mill Rd. Suite 610<br>
      Dallas, TX 75391
    </address>
  </section>
</main>
</body>
</html>
```